Landing Page Design for Adult Dating Age Verification (18+)

The objective of this task is to design a visually appealing pre-landing page for the adult dating site "Pivolunda (site: https://pivolunda.example/)" with an age verification mechanism. The pre-landing page will feature two buttons that redirect visitors to the main offer. The design should also include a footer block that includes links to the terms of use, privacy policy, and contact us pages.

Design Requirements:
Develop an age verification section prominently displayed on the pre-landing page.
Design the section to include two buttons labeled "Yes" and "No" for visitors to confirm their age.
Ensure the section is visually appealing and clearly communicates the purpose of age verification.

Visual Appeal:
Create a visually appealing design that aligns with the branding and theme of the "Pivolunda" adult dating site.
Use suitable color schemes, typography, and graphics to enhance the overall visual appeal of the pre-landing page.

Layout and Navigation:
Design an engaging and intuitive layout that encourages visitors to interact with the page and proceed to the main offer.
Ensure clear and visible navigation elements that direct visitors to the main offer or provide additional information.

Responsive Design:
Develop a responsive design that provides a seamless user experience across various devices, including desktop and mobile.
Ensure the design elements and layout adapt well to different screen sizes and resolutions.

File Formats and Assets:
Deliver the final design in PSD, AI, or Sketch format, ensuring that the files are well-organized and layered.
Include any necessary images or assets used in the design, ensuring they are of high quality and optimized for web use.

```html
<!DOCTYPE html>
<html lang="en">
<head>
<meta charset="utf-8">
<title>Pivolunda – Age Verification</title>
<link href="https://fonts.googleapis.com/css2?family=Montserrat:wght@600;800&family=Poppins:wght@400&family=Prata&family=Playfair+Display:wght@700&display=swap" rel="stylesheet">
<style>
  :root {
    --bg-dark: #1e1e1e;
    --bg-mid: #3a3a3a;
    --text-light: #ffffff;
    --accent-pink: #d98cf0;
    --accent-soft: #d7b4e6;
    --button-border: #9a9a9a;
    --button-text: #c8c8c8;
    --footer-text: #8a8a8a;
  }
  * { margin: 0; padding: 0; box-sizing: border-box; }
  html, body {
    width: 1200px;
    height: 669px;
    overflow: hidden;
    background: var(--bg-dark);
  }
  .age-gate {
    position: relative;
    width: 1200px;
    height: 669px;
    overflow: hidden;
  }
  .age-gate__backdrop {
    position: absolute;
    inset: 0;
    background:
      radial-gradient(ellipse 45% 60% at 40% 55%, #3c3c3c 0%, transparent 70%),
      radial-gradient(ellipse 35% 45% at 78% 65%, #363636 0%, transparent 70%),
      linear-gradient(180deg, #2b2b2b 0%, var(--bg-mid) 75%, #444 100%);
  }
  .brand {
    position: absolute;
    top: 137px;
    left: 0;
    width: 100%;
    display: flex;
    justify-content: center;
    align-items: center;
    gap: 8px;
  }
  .brand__dot {
    width: 28px;
    height: 28px;
    border-radius: 50%;
    background: var(--accent-soft);
  }
  .brand__name {
    font-family: "Playfair Display", serif;
    font-weight: 700;
    font-size: 18px;
    color: var(--text-light);
  }
  .headline {
    position: absolute;
    top: 200px;
    left: 0;
    width: 100%;
    display: flex;
    justify-content: center;
    align-items: baseline;
    gap: 16px;
    color: var(--text-light);
    line-height: 1;
  }
  .headline__intro {
    font-family: "Montserrat", sans-serif;
    font-weight: 800;
    font-size: 46px;
    letter-spacing: -0.5px;
  }
  .headline__brand {
    font-family: "Poppins", sans-serif;
    font-weight: 400;
    font-size: 84px;
    color: transparent;
    -webkit-text-stroke: 1.5px var(--accent-pink);
    letter-spacing: 0;
  }
  .question {
    position: absolute;
    top: 342px;
    left: 0;
    width: 100%;
    text-align: center;
    font-family: "Prata", serif;
    font-size: 28px;
    color: var(--text-light);
    letter-spacing: -0.3px;
  }
  .choices {
    position: absolute;
    top: 400px;
    left: 0;
    width: 100%;
    display: flex;
    justify-content: center;
    gap: 12px;
  }
  .choice {
    width: 49px;
    height: 49px;
    border-radius: 50%;
    border: 1px solid var(--button-border);
    background: transparent;
    color: var(--button-text);
    font-family: "Montserrat", sans-serif;
    font-weight: 600;
    font-size: 10px;
    display: flex;
    align-items: center;
    justify-content: center;
    text-decoration: none;
  }
  .site-footer {
    position: absolute;
    bottom: 22px;
    left: 0;
    width: 100%;
    display: flex;
    justify-content: center;
    gap: 28px;
  }
  .site-footer__link {
    font-family: "Montserrat", sans-serif;
    font-weight: 600;
    font-size: 10px;
    letter-spacing: 0.6px;
    text-transform: uppercase;
    color: var(--footer-text);
    text-decoration: none;
  }
</style>
</head>
<body>
  <main class="age-gate">
    <div class="age-gate__backdrop" role="img" aria-label="Dimmed black-and-white photo of a woman sitting on white bed sheets, seen from behind"></div>

    <div class="brand">
      <span class="brand__dot"></span>
      <span class="brand__name">Pivolunda</span>
    </div>

    <h1 class="headline">
      <span class="headline__intro">WELCOME TO</span>
      <span class="headline__brand">PIVOLUNDA</span>
    </h1>

    <p class="question">Are you older than 18?</p>

    <nav class="choices">
      <a class="choice" href="#">NO</a>
      <a class="choice" href="https://pivolunda.example/">YES</a>
    </nav>

    <footer class="site-footer">
      <a class="site-footer__link" href="https://pivolunda.example/terms">Terms of Use</a>
      <a class="site-footer__link" href="https://pivolunda.example/privacy">Privacy Policy</a>
      <a class="site-footer__link" href="https://pivolunda.example/contact">Contact Us</a>
    </footer>
  </main>
</body>
</html>
```